Flyer für Hersteller von Designertischen
Zielgruppe
Wir bauen Designer Tische, unser Zielgruppe liegt zwischen 35 und 50 Jahren
Aufgabenstellung
Wir legen Wert auf ein minimales Design, gerne in dem Stil unserer Website

```html
<!DOCTYPE html>
<html lang="de">
<head>
<meta charset="utf-8">
<title>Lindqvist Manufaktur – Flyer</title>
<link rel="stylesheet" href="https://fonts.googleapis.com/css2?family=Poppins:wght@300;400;500;700;800&display=swap">
<style>
  :root {
    --backdrop: #b3b3b3;
    --paper: #f4f5f7;
    --ink: #111111;
    --black: #000000;
    --white: #ffffff;
    --gold: #e0bc7a;
    --wood-light: #c99a5c;
    --wood-dark: #2a1c10;
  }
  * { box-sizing: border-box; margin: 0; padding: 0; }
  html, body { width: 1200px; height: 1200px; overflow: hidden; }
  body {
    background: var(--backdrop);
    font-family: "Poppins", sans-serif;
    color: var(--ink);
    position: relative;
  }
  .flyer {
    position: absolute;
    left: 200px; top: 40px;
    width: 800px; height: 1120px;
    background: var(--paper);
    overflow: hidden;
  }
  .brand {
    position: absolute;
    left: 0; top: 0; width: 320px; height: 266px;
    display: flex; flex-direction: column; align-items: center; justify-content: center;
    gap: 12px;
  }
  .brand-ring {
    width: 110px; height: 110px; border-radius: 50%;
    border: 6px solid #222;
  }
  .brand-name {
    font-size: 12px; font-weight: 400; letter-spacing: 0.25em;
    text-transform: uppercase; color: #222;
  }
  .headline {
    position: absolute;
    left: 320px; top: 0; width: 480px; height: 266px;
    background: var(--black); color: var(--white);
    padding: 44px 0 0 45px;
    font-size: 53px; line-height: 65px;
  }
  .headline strong { display: block; font-weight: 800; }
  .headline span { display: block; font-weight: 300; }
  .photo { position: absolute; }
  .photo-edge {
    left: 0; top: 289px; width: 320px; height: 272px;
    background: radial-gradient(ellipse at 45% 50%, var(--wood-light) 0%, #6a4a28 35%, var(--wood-dark) 75%, #0d0905 100%);
  }
  .photo-front {
    left: 0; top: 589px; width: 320px; height: 272px;
    background: radial-gradient(ellipse at 50% 40%, #d6a86a 0%, #5a4428 30%, #1a140c 65%, #070604 100%);
  }
  .photo-tunnel {
    left: 360px; top: 653px; width: 440px; height: 399px;
    background: linear-gradient(160deg, #7d7248 0%, #a08a58 30%, #5b5436 60%, #2f2a1c 100%);
  }
  .section { position: absolute; left: 362px; width: 397px; }
  .section h2 {
    font-size: 22px; font-weight: 700; line-height: 28px;
    text-transform: uppercase; margin-bottom: 8px;
  }
  .section p {
    font-size: 11.6px; line-height: 18.2px; text-align: justify;
    font-weight: 400;
  }
  .about { top: 392px - 0px; }
  .about { top: 296px; }
  .why { top: 592px - 0px; }
  .why { top: 590px - 0px; }
  .why { top: 591px; top: 590px; }
  .contact-bar {
    position: absolute; left: 0; top: 881px; width: 320px; height: 34px;
    background: var(--gold);
    padding-left: 37px;
    font-size: 21px; font-weight: 700; line-height: 34px;
  }
  .contact-list {
    position: absolute; left: 38px; top: 931px;
    list-style: none; font-size: 12px; line-height: 23.5px;
  }
  .footer-band {
    position: absolute; left: 0; top: 1052px; width: 800px; height: 68px;
    background: var(--gold);
    display: flex; align-items: center; padding-left: 42px; gap: 14px;
  }
  .footer-mark {
    width: 29px; height: 29px; border: 3px solid var(--ink); border-radius: 7px;
  }
  .footer-handle {
    font-size: 12px; font-weight: 700; letter-spacing: 0.32em;
  }
</style>
</head>
<body>
  <main class="flyer">
    <div class="brand">
      <div class="brand-ring"></div>
      <div class="brand-name">Lindqvist Manufaktur</div>
    </div>

    <header class="headline">
      <strong>MÖBEL DIE</strong>
      <span>GESCHICHTEN</span>
      <span>ERZÄHLEN</span>
    </header>

    <div class="photo photo-edge" role="img" aria-label="Nahaufnahme der Tischkante aus Massivholz mit eingelassener Plakette in einem dunklen Tunnel"></div>
    <div class="photo photo-front" role="img" aria-label="Holztisch mit schwarzen Metallbeinen von vorne in einem dunklen Gewölbe"></div>

    <section class="section about" style="top:386px">
      <h2>Über mich</h2>
      <p>Ich bin Jonas Lindqvist und Gründer der Lindqvist Manufaktur. Mein Vater war Holzbildhauer, wodurch ich bereits in früher Kindheit mit dem Material Holz in Kontakt kam und seither Techniken der Holzbearbeitung erlernte. Inzwischen habe ich mich auf die Arbeit mit Holzmonolithen spezialisiert, also die Herstellung von Esstischen die aus einer einzigen großen Bohle geschaffen werden. Darüber hinaus stellen wir leidenschaftlich gerne Couchtische, Waschtischplatten und Konferenztische her.</p>
    </section>

    <section class="section why" style="top:588px">
      <h2>Warum uns<br>wählen?</h2>
      <p>Unsere Leidenschaft ist es, zeitlose und langlebige Möbel zu schaffen. Jeder unserer Tische wird mit Sorgfalt und Liebe zum Detail gefertigt, um ein Leben lang zu bestehen. Qualität und Beständigkeit sind dabei unser oberstes Ziel.</p>
    </section>

    <div class="photo photo-tunnel" role="img" aria-label="Langer Holztisch mit schwarzen Metallbeinen in einem beleuchteten Betontunnel"></div>

    <div class="contact-bar">KONTAKT</div>
    <ul class="contact-list">
      <li>Lindqvist Manufaktur</li>
      <li>Ahornweg 14, 70000 Musterstadt</li>
      <li>TEL: 0150/00000000</li>
      <li>Email: kontakt@lindqvist-manufaktur.de</li>
    </ul>

    <footer class="footer-band">
      <div class="footer-mark"></div>
      <div class="footer-handle">LINDQVIST-MANUFAKTUR</div>
    </footer>
  </main>
</body>
</html>
```